Create a professional label for a retail product

Looking to get a 4.2 x 5 label designed for a new one of our products. We are an oral hygiene company and need the design to be professional and with it. The label is going to be clear going on an aluminum bottle. You can see our logo and company products at www.brivelrinse.com

I have attached both our company logo and existing label.

Target Market(s)

Retail, dentists

Industry/Entity Type

Retail

Colors
33a6d7
ffffff

Requirements
Must have
• Logo, FDA registered badge, Made in US badge, Patent pending badge.

```html
<!DOCTYPE html>
<html lang="en">
<head>
<meta charset="utf-8">
<title>Brivel Rinse Label</title>
<link rel="stylesheet" href="https://fonts.googleapis.com/css2?family=Montserrat:wght@400;600;700;800&family=Questrial&display=swap">
<style>
  :root {
    --brand-blue: #33a6d7;
    --white: #ffffff;
    --ink: #1a1a1a;
    --steel-light: #d6d8da;
    --steel-mid: #aeb1b4;
    --steel-dark: #8d9093;
    --page: #ffffff;
    --floor: #e6e6e6;
  }
  * { box-sizing: border-box; margin: 0; padding: 0; }
  html, body { width: 1200px; height: 1000px; overflow: hidden; }
  body {
    background: linear-gradient(to bottom, var(--page) 0%, var(--page) 78%, var(--floor) 100%);
    font-family: "Questrial", sans-serif;
    position: relative;
  }

  /* ---------- Presentation column ---------- */
  .wordmark {
    position: absolute; left: 55px; top: 105px;
    display: flex; align-items: center; gap: 14px; white-space: nowrap;
  }
  .wordmark-dot { width: 30px; height: 30px; border-radius: 50%; background: var(--brand-blue); flex: none; }
  .wordmark-name {
    font-family: "Montserrat", sans-serif; font-weight: 800;
    font-size: 38px; line-height: 1; color: var(--brand-blue); letter-spacing: 0.5px;
  }
  .claim-banner {
    position: absolute; left: 50px; top: 232px; width: 370px; height: 81px;
    background: var(--brand-blue); color: var(--white); text-align: center; padding-top: 9px;
  }
  .claim-title { font-family: "Montserrat", sans-serif; font-weight: 700; font-size: 26px; line-height: 1.2; white-space: nowrap; }
  .claim-sub { font-family: "Montserrat", sans-serif; font-weight: 400; font-size: 20px; line-height: 1.3; letter-spacing: 0.5px; white-space: nowrap; }
  .benefit-list { position: absolute; left: 64px; top: 333px; list-style: none; }
  .benefit-list li {
    display: flex; align-items: center; gap: 10px;
    color: var(--brand-blue); font-size: 17.5px; height: 41px; white-space: nowrap;
  }
  .benefit-list svg { width: 20px; height: 20px; flex: none; color: var(--brand-blue); }
  .safe-badge {
    position: absolute; border-radius: 50%;
    background: var(--brand-blue); border: 5px solid var(--white);
    box-shadow: 0 0 0 4px var(--brand-blue);
    display: flex; flex-direction: column; align-items: center; justify-content: center;
    color: var(--white); font-family: "Montserrat", sans-serif; font-weight: 800; line-height: 1;
  }
  .panel-badge { left: 180px; top: 470px; width: 110px; height: 110px; }
  .safe-badge .pct { font-size: 25px; }
  .safe-badge .word { font-size: 24px; }
  .gel-tag {
    position: absolute; left: 60px; top: 614px; width: 315px; text-align: center;
    font-family: "Montserrat", sans-serif; font-weight: 800; font-size: 25px;
    color: var(--brand-blue); white-space: nowrap;
    background: linear-gradient(to right, transparent, #e2e2e2 15%, #e2e2e2 85%, transparent);
    padding: 3px 0;
  }
  .bracket { color: var(--ink); font-weight: 400; }

  /* ---------- Flat labels ---------- */
  .label {
    position: absolute; width: 170px;
    background: linear-gradient(to right, var(--steel-dark), var(--steel-light) 45%, var(--steel-mid));
    overflow: hidden;
  }
  .label-front { left: 525px; top: 315px; height: 630px; }
  .label-back { left: 885px; top: 315px; height: 635px; }
  .label .texture {
    position: absolute; left: 0; right: 0; top: 0; height: 70px;
    background: linear-gradient(to bottom, #eef0f1, transparent);
  }
  .label > * { position: absolute; }
  .label-wordmark {
    left: 0; right: 0; display: flex; align-items: center; justify-content: center; gap: 5px;
    font-family: "Montserrat", sans-serif; font-weight: 800; font-size: 17px; color: var(--brand-blue); white-space: nowrap;
  }
  .label-wordmark .wordmark-dot { width: 12px; height: 12px; }
  .label-front .label-wordmark { top: 130px; }
  .label-back .label-wordmark { top: 135px; }
  .label-banner {
    left: 0; right: 0; height: 42px;
    background: var(--brand-blue); color: var(--white); text-align: center; padding-top: 5px;
  }
  .label-front .label-banner { top: 218px; }
  .label-back .label-banner { top: 275px; }
  .label-banner .claim-title { font-size: 12.5px; }
  .label-banner .claim-sub { font-size: 10px; letter-spacing: 0.2px; }
  .label-list { left: 12px; right: 4px; list-style: none; }
  .label-front .label-list { top: 276px; }
  .label-back .label-list { top: 343px; }
  .label-list li { display: flex; align-items: center; gap: 6px; height: 29px; color: var(--white); font-size: 10.5px; white-space: nowrap; }
  .label-list svg { width: 13px; height: 13px; flex: none; }
  .label .safe-badge { border-width: 3px; box-shadow: 0 0 0 2px var(--brand-blue); }
  .label-front .safe-badge { left: 48px; top: 388px; width: 74px; height: 74px; }
  .label-back .safe-badge { left: 45px; top: 495px; width: 80px; height: 80px; }
  .label .safe-badge .pct { font-size: 17px; }
  .label .safe-badge .word { font-size: 16px; }
  .label-gel {
    left: 50%; transform: translateX(-50%);
    background: var(--white); color: var(--brand-blue); white-space: nowrap;
    font-family: "Montserrat", sans-serif; font-weight: 800; font-size: 12.5px; padding: 1px 4px;
  }
  .label-front .label-gel { top: 508px; }
  .label-back .label-gel { top: 441px; }
  .label-foot {
    left: 0; right: 0; bottom: 0;
    background: var(--brand-blue); color: var(--white); text-align: center; padding-top: 16px;
    font-family: "Montserrat", sans-serif;
  }
  .label-front .label-foot { height: 65px; }
  .label-back .label-foot { height: 55px; padding-top: 12px; }
  .label-foot .scent { font-weight: 700; font-size: 12px; }
  .label-foot .volume { font-size: 8.5px; }
</style>
</head>
<body>

<svg width="0" height="0" style="position:absolute" aria-hidden="true">
  <symbol id="tick" viewBox="0 0 20 20">
    <path d="M2 10.5 L7.5 16 L18 3.5" fill="none" stroke="currentColor" stroke-width="3.2" stroke-linecap="round" stroke-linejoin="round"/>
  </symbol>
  <symbol id="checkbox" viewBox="0 0 14 14">
    <rect x="1" y="2" width="11" height="11" fill="none" stroke="#ffffff" stroke-width="1.4"/>
    <path d="M3.5 7.5 L6 10 L13 1.5" fill="none" stroke="#33a6d7" stroke-width="2" stroke-linecap="round"/>
  </symbol>
</svg>

<section class="brand-panel">
  <div class="wordmark">
    <span class="wordmark-dot"></span>
    <span class="wordmark-name">BRIVEL RINSE</span>
  </div>
  <div class="claim-banner">
    <div class="claim-title">CLEANS AND STERILIZES</div>
    <div class="claim-sub">ALL ORTHODONTIC DEVICES</div>
  </div>
  <ul class="benefit-list">
    <li><svg><use href="#tick"/></svg>Superfast 60 Secound Clean</li>
    <li><svg><use href="#tick"/></svg>Anti-viral, Anti Bacterial, Anti-fungal</li>
    <li><svg><use href="#tick"/></svg>Goes Anywhere You Go</li>
  </ul>
  <div class="safe-badge panel-badge"><span class="pct">100%</span><span class="word">SAFE</span></div>
  <div class="gel-tag"><span class="bracket">[ </span>DEEP CLEAN GEL<span class="bracket"> ]</span></div>
</section>

<article class="label label-front">
  <div class="texture" role="img" aria-label="Brushed aluminium surface with fading dot pattern"></div>
  <div class="label-wordmark"><span class="wordmark-dot"></span>BRIVEL RINSE</div>
  <div class="label-banner">
    <div class="claim-title">CLEANS AND STERILIZES</div>
    <div class="claim-sub">ALL ORTHODONTIC DEVICES</div>
  </div>
  <ul class="label-list">
    <li><svg><use href="#checkbox"/></svg>Superfast 60 Secound Clean</li>
    <li><svg><use href="#checkbox"/></svg>Anti-viral, Anti Bacterial</li>
    <li><svg><use href="#checkbox"/></svg>Goes Anywhere You Go</li>
  </ul>
  <div class="safe-badge"><span class="pct">100%</span><span class="word">SAFE</span></div>
  <div class="label-gel"><span class="bracket">[</span>DEEP CLEAN GEL<span class="bracket">]</span></div>
  <div class="label-foot">
    <div class="scent">MINT SCENT</div>
    <div class="volume">3.38 FL OZ (100 ml)</div>
  </div>
</article>

<article class="label label-back">
  <div class="texture" role="img" aria-label="Brushed aluminium surface with fading dot pattern"></div>
  <div class="label-wordmark"><span class="wordmark-dot"></span>BRIVEL RINSE</div>
  <div class="label-banner">
    <div class="claim-title">CLEANS AND STERILIZES</div>
    <div class="claim-sub">ALL ORTHODONTIC DEVICES</div>
  </div>
  <ul class="label-list">
    <li><svg><use href="#checkbox"/></svg>Superfast 60 Secound Clean</li>
    <li><svg><use href="#checkbox"/></svg>Anti-viral, Anti Bacterial</li>
    <li><svg><use href="#checkbox"/></svg>Goes Anywhere You Go</li>
  </ul>
  <div class="label-gel"><span class="bracket">[</span>DEEP CLEAN GEL<span class="bracket">]</span></div>
  <div class="safe-badge"><span class="pct">100%</span><span class="word">SAFE</span></div>
  <div class="label-foot">
    <div class="scent">MINT SCENT</div>
    <div class="volume">3.38 FL OZ (100 ml)</div>
  </div>
</article>

</body>
</html>
```